500ml Aluminium drinking Water Bottle. Endlessly reusable and refillable

We need a label for our new 500ml water bottle. We are Corrie Vale Springs based in the Scottish Highlands. We extract filter and bottle drinking water from Loch Ness in Scotland. We currently have on the market a 100ml bottle of water designed for whisky drinkers see - www.fernhollowaqua.example
We now want to create a 500ml bottle of still and sparkling water using aluminium bottles which allows us much more room for branding. Our water will be exclusive and high end, not available in the supermarkets only selected outlets. Our current branding is based on the the number Corrie Vale which relates to the depth of the Loch at Corrie Vale Fathoms. We have interwound the legendary loch ness monster into the top half of the numbers. We will use the Corrie Vale logo on our new 500ml product but need a creative approach as to how it is presented on the bottle. Our 100ml Dew for Drams" product will stand alone, our new 500ml will use the same Corrie Vale logo, but its strap line will be changed to differentiate between our products. We need to maximise the available space on the aluminium bottle to ensure our product leaps out at the consumer. The available space for the new branding is 207mm wide x 120mm high, but in this space we need allow room for our barcode, address and statutory information, but we can scale these up or down. Our new design will be exclusive and elegant, not loud or harsh. It will represent a unique drinking water product from an iconic water source. So the branding of Corrie Vale is supplied. Our target consumer is middle aged and above with a disposable income,, those who want to experience rare and exclusive products and who are prepared to pay for that luxury.
Updates

Hi Guys - please fee free to use the Corrie Vale logo, but leave out "Dew for Drams". We are trying to create a label for 500ml aluminium bottles of still and sparkling drinking water for any occasion. We need the label design to be bold and vibrant but not brash or harsh. We are targeting exclusive retail and high end dining outlets, where the consumer will appreciate the pure water from the Scottish highlands. The history and scenery of Scotland should provide some inspiration for your designs or colour palette. We want to invoke thoughts of cold clear water and the refreshing taste of our pure water.

Target Market(s)

Exclusive high end consumers

Industry/Entity Type

food and drink

Requirements
Must have
• clear bright color scheme clever positioning of the logo
Should not have
• the term "Loch Ness Water" must not appear

```html
<!DOCTYPE html>
<html lang="en">
<head>
<meta charset="utf-8">
<title>Corrie Vale Springs – 500ml Label</title>
<link href="https://fonts.googleapis.com/css2?family=Montserrat:wght@400;500&display=swap" rel="stylesheet">
<style>
  :root {
    --backdrop: #e4e5e7;
    --label-deep: #1d5658;
    --label-band: #3e7e7a;
    --mint: #7cc1b3;
    --white: #f4f7f7;
  }
  * { box-sizing: border-box; margin: 0; padding: 0; }
  html, body {
    width: 1200px;
    height: 1200px;
    overflow: hidden;
    background: var(--backdrop);
  }
  .canvas {
    width: 1200px;
    height: 1200px;
    display: flex;
    align-items: center;
    justify-content: center;
  }
  .label {
    width: 560px;
    height: 860px;
    background: var(--label-deep);
    display: flex;
    flex-direction: column;
    align-items: center;
    font-family: "Montserrat", sans-serif;
  }
  .label-main {
    flex: 1;
    width: 100%;
    display: flex;
    flex-direction: column;
    align-items: center;
    padding-top: 150px;
  }
  .brand-name {
    font-weight: 500;
    font-size: 88px;
    line-height: 1;
    color: var(--white);
    letter-spacing: 0.01em;
    display: flex;
    align-items: flex-start;
    gap: 10px;
  }
  .brand-name .mark {
    width: 14px;
    height: 14px;
    border: 2px solid var(--mint);
    border-radius: 50%;
    margin-top: 4px;
  }
  .strapline {
    margin-top: 44px;
    font-weight: 400;
    font-size: 25px;
    letter-spacing: 0.02em;
    color: var(--mint);
    text-transform: uppercase;
  }
  .wave-art {
    margin-top: 118px;
    width: 330px;
    height: 200px;
    background: linear-gradient(180deg, var(--mint) 0%, var(--white) 35%, var(--mint) 65%, var(--white) 100%);
    opacity: 0.55;
  }
  .volume-band {
    width: 100%;
    height: 130px;
    background: var(--label-band);
    display: flex;
    align-items: center;
    justify-content: center;
  }
  .volume {
    font-size: 36px;
    font-weight: 400;
    color: var(--white);
    letter-spacing: 0.03em;
  }
  .volume .unit { font-size: 26px; }
</style>
</head>
<body>
  <main class="canvas">
    <section class="label">
      <div class="label-main">
        <h1 class="brand-name">Corrie Vale<span class="mark" aria-hidden="true"></span></h1>
        <p class="strapline">Pure Natural Water</p>
        <div class="wave-art" role="img" aria-label="Stacked wavy lines suggesting water ripples in mint and white"></div>
      </div>
      <div class="volume-band">
        <p class="volume">500<span class="unit">ML</span> ℮</p>
      </div>
    </section>
  </main>
</body>
</html>
```